specialised legal consultancy business needs an update on logo and office stationary.

Update on Logo - see attached.

update on email signature - something new and fresh with only the following details -

(the logo)
Advocate Karel Steenkamp
KS Venture Frameworks (Pty) Ltd (Reg No.: 2019 / 374915 / 07)
LLB, LLM (Cum Laude), Cert.Dir (ABNQE), FCG (PTVRO)
+27 82 596 1174
karel#veldanvik.com

Update on letterhead - something new and fresh and please more user-friendly. With the same details as per the email signature.

```html
<!DOCTYPE html>
<html lang="en">
<head>
<meta charset="utf-8">
<title>Email Signature – Advocate Karel Steenkamp</title>
<link rel="stylesheet" href="https://fonts.googleapis.com/css2?family=Montserrat:wght@600;700&family=Pinyon+Script&family=Source+Sans+3:wght@400&display=swap">
<style>
  :root {
    --brand-blue: #2383ad;
    --ink: #333333;
    --paper: #ffffff;
  }
  html, body {
    margin: 0;
    padding: 0;
    overflow: hidden;
    background: var(--paper);
  }
  .signature {
    position: relative;
    width: 1200px;
    height: 499px;
    background: var(--paper);
    overflow: hidden;
    color: var(--ink);
  }
  .brand-mark {
    position: absolute;
    left: 209px;
    top: 66px;
    width: 130px;
    height: 130px;
    background: var(--brand-blue);
  }
  .brand-name {
    position: absolute;
    left: 177px;
    top: 228px;
    margin: 0;
    font-family: "Montserrat", sans-serif;
    font-weight: 700;
    font-size: 20px;
    letter-spacing: 2.6px;
    line-height: 1;
    color: var(--ink);
    white-space: nowrap;
  }
  .advocate-name {
    position: absolute;
    left: 176px;
    top: 274px;
    margin: 0;
    font-family: "Pinyon Script", cursive;
    font-weight: 400;
    font-size: 34px;
    line-height: 1.2;
    color: var(--brand-blue);
    white-space: nowrap;
  }
  .credentials {
    position: absolute;
    left: 175px;
    top: 322px;
    margin: 0;
    font-family: "Source Sans 3", sans-serif;
    font-size: 15px;
    line-height: 19px;
    color: var(--ink);
    white-space: nowrap;
  }
  .contact-list {
    position: absolute;
    left: 175px;
    top: 370px;
    margin: 0;
    padding: 0;
    list-style: none;
  }
  .contact-item {
    display: flex;
    align-items: center;
    height: 25px;
    font-family: "Montserrat", sans-serif;
    font-weight: 600;
    font-size: 19px;
    letter-spacing: -0.3px;
    color: var(--ink);
  }
  .contact-icon {
    width: 21px;
    height: 17px;
    margin-right: 20px;
    flex: none;
  }
</style>
</head>
<body>
  <main class="signature">
    <div class="brand-mark" aria-hidden="true"></div>
    <p class="brand-name">KS FRAMEWORKS</p>

    <h1 class="advocate-name">Advocate Karel Steenkamp</h1>

    <p class="credentials">
      KS Venture Frameworks (Pty) Ltd (Reg No.: 2019 / 374915 / 07)<br>
      LLB, LLM (Cum Laude), Cert.Dir (ABNQE), FCG (PTVRO)
    </p>

    <ul class="contact-list">
      <li class="contact-item">
        <svg class="contact-icon" viewBox="0 0 21 17" aria-hidden="true">
          <path d="M1 5 C1 1 20 1 20 5 L20 6.5 L15 6.5 L15 4.5 C12 3.5 9 3.5 6 4.5 L6 6.5 L1 6.5 Z" fill="var(--brand-blue)"/>
          <path d="M6 7 L15 7 L19 11 L19 16 L2 16 L2 11 Z" fill="var(--brand-blue)"/>
          <g fill="var(--paper)">
            <rect x="8" y="9" width="1.3" height="1.3"/>
            <rect x="10" y="9" width="1.3" height="1.3"/>
            <rect x="12" y="9" width="1.3" height="1.3"/>
            <rect x="8" y="11" width="1.3" height="1.3"/>
            <rect x="10" y="11" width="1.3" height="1.3"/>
            <rect x="12" y="11" width="1.3" height="1.3"/>
            <rect x="8" y="13" width="1.3" height="1.3"/>
            <rect x="10" y="13" width="1.3" height="1.3"/>
            <rect x="12" y="13" width="1.3" height="1.3"/>
          </g>
        </svg>
        <span>+27 82 596 1174</span>
      </li>
      <li class="contact-item">
        <svg class="contact-icon" viewBox="0 0 21 17" aria-hidden="true">
          <rect x="0" y="0" width="21" height="17" rx="1" fill="var(--brand-blue)"/>
          <path d="M1.5 1.5 L10.5 9.5 L19.5 1.5 M1.5 15.5 L8 8 M19.5 15.5 L13 8" stroke="var(--paper)" stroke-width="1" fill="none"/>
        </svg>
        <span>karel@veldanvik.com</span>
      </li>
    </ul>
  </main>
</body>
</html>
```